I need a business card for my original fine art pieces

I would like a business card design including a logo design for a new business in the art world. I am based in the Hunter Valley NSW Australia. I am a contemporary figurative, encaustic and wildlife artist. I would like to be able to upload my email and mobile number to this as well. This design should be one that I can incorporate into banners and flyers etc. Id like to incorporate one of my own images or partial image into the background or somewhere below. My initials are KD and I would like these used as a logo type. I would like the use of some colour and it to be bright and catchy. The final design should communicate artwork custom made and commissions available.

Overview: Original Fine Artworks for sale, online, art galleries etc, Custom made to order and by commission.

Target market is world wide audience and corporate world

My figurative work is painted using acrylics in a lot of natural ochre colours that reflect the Australian Outback, on canvas, linen, paper or board: My encaustic work is created in a contemporary abstract style using a blow torch and a made with a medium of 100% pure bees wax, Damar resin, mixed media and coloured pigments, applied to Birch board. My wildlife are created using coloured pencil and mixed media on a variety of paper types or board.

```html
<!DOCTYPE html>
<html lang="en">
<head>
<meta charset="utf-8">
<title>Kira Dawson – Business Card</title>
<link rel="stylesheet" href="https://fonts.googleapis.com/css2?family=Lato:wght@400&family=Montserrat:wght@500&family=Tinos&display=swap">
<style>
  :root {
    --page-bg: #e9e7e4;
    --card-top: #fbfbfb;
    --card-bottom: #eeeeee;
    --brand-orange: #f4511e;
    --brand-orange-deep: #e9481a;
    --ink: #1c1c1c;
    --crescent: #1a1a1a;
    --white: #ffffff;
  }
  * { margin: 0; padding: 0; box-sizing: border-box; }
  html, body {
    width: 1200px; height: 900px; overflow: hidden;
    background: var(--page-bg);
  }
  .business-card {
    position: absolute; left: 150px; top: 172px;
    width: 900px; height: 556px;
    border-radius: 20px; overflow: hidden;
    background: linear-gradient(180deg, var(--card-top), var(--card-bottom));
    box-shadow: 0 10px 30px rgba(0,0,0,0.12);
  }
  .accent-shape { position: absolute; inset: 0; width: 900px; height: 556px; }
  .brand-name {
    position: absolute; left: 40px; top: 226px; width: 430px;
    text-align: center;
    font-family: "Tinos", serif; font-weight: 400;
    font-size: 50px; line-height: 1; color: var(--brand-orange);
    letter-spacing: 2px; text-transform: uppercase;
  }
  .brand-tagline {
    position: absolute; left: 44px; top: 292px; width: 426px;
    text-align: center;
    font-family: "Montserrat", sans-serif; font-weight: 500;
    font-size: 20px; letter-spacing: 5.4px; color: var(--ink);
  }
  .person-name {
    position: absolute; left: 50px; top: 352px;
    font-family: "Tinos", serif; font-weight: 400;
    font-size: 37px; line-height: 1.1; color: var(--brand-orange);
  }
  .person-role {
    position: absolute; left: 50px; top: 402px;
    font-family: "Lato", sans-serif; font-size: 23px; color: var(--ink);
  }
  .postal-address {
    position: absolute; left: 50px; top: 444px;
    font-family: "Lato", sans-serif; font-size: 23px; line-height: 29px;
    color: var(--ink); font-style: normal;
  }
  .contact-list {
    position: absolute; right: 44px; top: 248px;
    list-style: none; text-align: right;
    font-family: "Lato", sans-serif; font-size: 23px; line-height: 33px;
    color: var(--white);
  }
  .contact-list li { display: flex; align-items: center; justify-content: flex-end; gap: 8px; }
  .contact-icon { width: 17px; height: 17px; fill: var(--white); }
</style>
</head>
<body>
  <section class="business-card">
    <svg class="accent-shape" viewBox="0 0 900 556" aria-hidden="true">
      <defs>
        <linearGradient id="orangeFill" x1="0" y1="0" x2="1" y2="1">
          <stop offset="0" stop-color="#f86226"/>
          <stop offset="1" stop-color="#e9481a"/>
        </linearGradient>
      </defs>
      <circle cx="807" cy="282" r="296" fill="#1a1a1a"/>
      <circle cx="819" cy="280" r="293" fill="#f5f5f5"/>
      <circle cx="826" cy="280" r="292" fill="url(#orangeFill)"/>
    </svg>

    <h1 class="brand-name">Kira Dawson</h1>
    <p class="brand-tagline">ORIGINAL FINE ARTWORKS</p>

    <h2 class="person-name">Liam Carter</h2>
    <p class="person-role">Managing Director</p>
    <address class="postal-address">18 Wattle Street, Cessnock NSW<br>Australia, 2325</address>

    <ul class="contact-list">
      <li>(061)987654321
        <svg class="contact-icon" viewBox="0 0 24 24"><path d="M3 9c0-3 4-5 9-5s9 2 9 5v2h-5V9H8v2H3zM6 12h12l2 8H4z"/></svg>
      </li>
      <li>hello@kdartworks.com
        <svg class="contact-icon" viewBox="0 0 24 24"><path d="M2 5h20v14H2zM4 7v1l8 5 8-5V7l-8 5z"/></svg>
      </li>
      <li>www.kdartworks.com
        <svg class="contact-icon" viewBox="0 0 24 24"><circle cx="12" cy="12" r="10"/><path d="M12 2v20M2 12h20" stroke="#f4511e" stroke-width="1.6" fill="none"/></svg>
      </li>
    </ul>
  </section>
</body>
</html>
```